Pebble Shift

Text is below. 4x6 single sided is fine (web flyer).
I don't have a firm idea for the design but I want it to have a spring fresh feel to it since the weather is getting nice. Light colors would be nice. A non-slutty girl is always good too, it's more of a professional house music type function. I attached my logo and the old flyer (not very good, just attached for the rust room logo) and some other flyers that I've chosen through sketchhive. You can start with the background/image and PEBBLE SHIFT and add the text in later if you want to save time so I can tell you if I like the idea first. Thanks!
The Lantern Folk presents
PEBBLE SHIFT
WEDNESDAY 4/17/13
530-9PM
DECOMPRESS. INVIGORATE. REJUVENATE
Inside RUST ROOM (logo)
Join resident deejay NIKOS VARGA (facebook.com/lanternfolkhq) along with special guest this week:
ORBITA (Special UK Garage Set starting at 630pm) (logo)
(facebook.com/orbita42)
PEBBLE SHIFT is a weekly after-work chill-out lounge event for professionals, and sharp movers & shakers with sophisticated musical tastes.
Target Market(s)
Professionals and house music lovers, lounge atmosphere
Industry/Entity Type
House

```html
<!DOCTYPE html>
<html lang="en">
<head>
<meta charset="utf-8">
<title>Pebble Shift — Flyer</title>
<link rel="stylesheet" href="https://fonts.googleapis.com/css2?family=Archivo+Black&family=Almendra+Display&display=swap">
<style>
  :root {
    --sand: #d6c796;
    --sand-pale: #ddd3a6;
    --teal: #2b9aa3;
    --teal-deep: #1f7f8a;
    --teal-mist: #7fbfb8;
    --rust: #d0692f;
    --plum: #5a2c5c;
    --ink: #0b0b0b;
    --chalk: #ffffff;
  }
  * { margin: 0; padding: 0; box-sizing: border-box; }
  html, body { width: 816px; height: 1200px; overflow: hidden; background: var(--sand); }
  .flyer {
    position: relative;
    width: 816px;
    height: 1200px;
    overflow: hidden;
    background:
      radial-gradient(ellipse 260px 520px at 700px 720px, var(--teal) 0%, rgba(43,154,163,0) 100%),
      radial-gradient(ellipse 420px 300px at 520px 230px, var(--teal-deep) 0%, rgba(31,127,138,0) 100%),
      radial-gradient(ellipse 220px 420px at 380px 700px, var(--teal-mist) 0%, rgba(127,191,184,0) 100%),
      radial-gradient(ellipse 150px 90px at 250px 410px, rgba(90,44,92,.75) 0%, rgba(90,44,92,0) 100%),
      linear-gradient(90deg, var(--sand-pale) 0%, var(--teal-mist) 35%, var(--teal) 70%, var(--sand) 100%);
  }
  .art { position: absolute; }
  .art--trumpet { left: 473px; top: 64px; width: 170px; height: 96px; border-radius: 40px;
    background: linear-gradient(90deg, rgba(255,255,255,.75), rgba(230,190,170,.8)); }
  .art--flute { left: 40px; top: 312px; width: 750px; height: 22px; border-radius: 8px;
    background: linear-gradient(180deg, #6a4a6a, #3b2740); }
  .art--florals { left: 50px; top: 480px; width: 380px; height: 660px; border-radius: 48% 40% 30% 30%;
    background: radial-gradient(ellipse at 50% 45%, rgba(208,105,47,.8), rgba(208,105,47,0) 72%); }
  .art--clock { left: 377px; top: 563px; width: 186px; height: 148px;
    background: linear-gradient(180deg, rgba(140,95,40,.55), rgba(140,95,40,.25)); }
  .art--violin { left: 0; top: 697px; width: 237px; height: 460px; border-radius: 45% 45% 40% 40%;
    background: radial-gradient(ellipse at 55% 60%, rgba(255,255,255,.85), rgba(220,235,235,.25) 75%); }
  .art--swirl { left: 520px; top: 1010px; width: 110px; height: 150px; border-radius: 50%;
    background: radial-gradient(circle, rgba(255,255,255,.5), rgba(255,255,255,0) 70%); }

  .strokes { position: absolute; inset: 0; }

  .guest {
    position: absolute; left: 52px; top: 96px; width: 420px;
    display: flex; flex-direction: column; align-items: center;
  }
  .guest__name {
    display: flex; align-items: center; gap: 16px;
    font-family: "Archivo Black", sans-serif; font-size: 78px; line-height: 1;
    color: var(--ink);
  }
  .guest__mark { width: 22px; height: 22px; background: var(--ink); }
  .guest__genres {
    margin-top: 10px;
    font-family: "Archivo Black", sans-serif; font-size: 17px;
    color: var(--ink); word-spacing: 10px;
  }

  .title-first {
    position: absolute; left: 128px; top: 246px;
    font-family: "Archivo Black", sans-serif; font-size: 104px; line-height: 1;
    color: var(--ink); transform: rotate(17deg); transform-origin: left top;
    letter-spacing: -2px;
  }
  .title-second {
    position: absolute; left: 615px; top: 478px; width: 130px;
    display: flex; flex-direction: column; align-items: center; gap: 20px;
    font-family: "Almendra Display", serif; color: var(--ink); line-height: 1;
    font-size: 108px;
  }
</style>
</head>
<body>
<main class="flyer">
  <div class="art art--trumpet" role="img" aria-label="Sketched trumpet bell"></div>
  <div class="art art--florals" role="img" aria-label="Painted orange scroll and foliage ornaments"></div>
  <div class="art art--clock" role="img" aria-label="Faded grandfather clock sketch"></div>
  <div class="art art--flute" role="img" aria-label="Engraved flute across the page"></div>
  <div class="art art--violin" role="img" aria-label="Textured white violin with bow"></div>
  <div class="art art--swirl" role="img" aria-label="Ornamental white swirl"></div>

  <svg class="strokes" width="816" height="1200" viewBox="0 0 816 1200" fill="none" stroke="var(--chalk)">
    <path d="M0 80 C180 30 300 10 420 0" stroke-width="5"/>
    <path d="M0 420 C200 330 420 330 560 420 C660 480 760 470 816 430" stroke-width="3"/>
    <path d="M0 470 C220 400 440 430 816 300" stroke-width="1.5"/>
    <path d="M0 250 C240 180 520 120 816 40" stroke-width="1.5"/>
    <path d="M0 300 C260 230 560 170 816 120" stroke-width="1"/>
    <path d="M440 745 C560 730 700 735 790 755 C760 880 640 1010 440 1060 C520 960 560 860 440 745 Z" stroke-width="3"/>
    <path d="M330 525 L330 1200" stroke-width="2"/>
    <path d="M345 520 L470 520 L470 1200" stroke-width="1.5"/>
    <path d="M170 20 C150 120 260 300 500 420" stroke-width="1.5"/>
  </svg>

  <div class="guest">
    <div class="guest__name"><span class="guest__mark"></span>ORBITA</div>
    <div class="guest__genres">house garage 2step</div>
  </div>

  <h1>
    <span class="title-first">Pebble</span>
    <span class="title-second"><span>S</span><span>h</span><span>i</span><span>f</span><span>t</span></span>
  </h1>
</main>
</body>
</html>
```